Sol Gorditas Digital Menu Boards

IF SELECTED, WINNER MAY BE HIRED FOR OTHER DESIGNS OF DIFFERENT STORES OF OUR COMPANY.

Task: Digital Menu Boards Design

Task description: We need designs for a Digital Menu to be displayed on two 42’’screens at Solgorditas, a fast-food restaurant in Guadalajara, Mexico. The menu redesign should communicate to our customers the experience of eating at our restaurant.

For avoiding the creation of videos, we are expecting several menu slides with the same text but with different images, simulating the effect of a video where the images are changing. This menu slides will be projected through a USB memory and a slideshow.

Attached files:
For the design, there are several documents attached to the task description:
1. Logo of the restaurant
2. Pictures of the restaurant
3. Example video of what we want to achieve through this menu slides.
4. Pictures of the actual menu board, to be replaced with the new designs.
5. Menu description (regular and breakfast menu)
6. Pictures of each element on the menu (We don’t have yet any breakfast pictures)
**The files are organized on a ZIP file.

Expected product:
For the regular menu,
• 2 menu slide designs for TACOS Y ESPECIALIDADES, where the text will be exactly the same but the images would differ.
• 2 menu slide designs for BEBIDAS Y EXTRAS, where the text will be exactly the same but the images would differ.
For the breakfast menu,
• 1 menu slide including all the menu
Total: 5 menu board slides.

Technical specs:
• You should send the editable file, med and high resolution JPGs for each design.
• The designs should fit perfectly on 42’’ screens.

```html
<!DOCTYPE html>
<html lang="es">
<head>
<meta charset="utf-8">
<title>Sol Gorditas — Desayunos</title>
<link rel="stylesheet" href="https://fonts.googleapis.com/css2?family=Oswald:wght@300;400;700&display=swap">
<style>
  :root {
    --bg-light: #f1eeeb;
    --bg-dark: #d6cdc5;
    --title-red: #e8492a;
    --label-ink: #1d1a18;
    --badge-red: #ee3d24;
    --badge-ring: #f7c21a;
    --badge-text: #ffffff;
    --logo-green: #8cc63f;
    --logo-ink: #b3261e;
    --dot-red: #ee4a2b;
    --dot-yellow: #f2c318;
    --dot-salmon: #f4806a;
    --dot-cyan: #2bb6e0;
  }
  * { margin: 0; padding: 0; box-sizing: border-box; }
  html, body { width: 1200px; height: 599px; overflow: hidden; }
  body { background: var(--bg-light); }
  .menu-board {
    position: relative;
    width: 1200px;
    height: 599px;
    overflow: hidden;
    background: linear-gradient(90deg, var(--bg-light) 0%, #e6e0da 45%, var(--bg-dark) 100%);
    font-family: "Oswald", sans-serif;
  }
  .food-photo { position: absolute; inset: 0; width: 1200px; height: 599px; }
  .menu-title {
    position: absolute;
    left: 300px; top: 6px; width: 300px;
    text-align: center;
    color: var(--title-red);
    font-weight: 700;
    font-size: 44px;
    letter-spacing: 1px;
  }
  .label {
    position: absolute;
    color: var(--label-ink);
    font-weight: 300;
    font-size: 39px;
    line-height: 1;
    white-space: nowrap;
  }
  .label.col-head { transform: translateX(-50%); }
  .label.row-head { left: 8px; }
  .price {
    position: absolute;
    width: 96px; height: 96px;
    margin: -48px 0 0 -48px;
    border-radius: 50%;
    background: var(--badge-red);
    border: 6px solid var(--badge-ring);
    color: var(--badge-text);
    font-weight: 700;
    font-size: 36px;
    display: flex; align-items: center; justify-content: center;
  }
  .brand {
    position: absolute;
    left: 657px; top: 20px;
    width: 164px; height: 164px;
    border-radius: 50%;
    background: var(--logo-green);
    border: 5px solid #f3f1e6;
    display: flex; align-items: center; justify-content: center;
    text-align: center;
  }
  .brand-name {
    color: var(--logo-ink);
    font-weight: 700;
    font-size: 28px;
    line-height: 1.05;
  }
  .dot { position: absolute; border-radius: 50%; }
  .dot.red { left: 664px; top: 163px; width: 78px; height: 78px; background: var(--dot-red); }
  .dot.yellow { left: 672px; top: 449px; width: 52px; height: 52px; background: var(--dot-yellow); }
  .dot.salmon { left: 735px; top: 447px; width: 100px; height: 100px; background: var(--dot-salmon); }
  .dot.cyan { left: 702px; top: 540px; width: 28px; height: 28px; background: var(--dot-cyan); }
</style>
</head>
<body>
<main class="menu-board">
  <svg class="food-photo" viewBox="0 0 1200 599" role="img" aria-label="Photo of red chilaquiles topped with avocado, radish, red onion, cilantro, cream, cheese and a fried egg">
    <defs>
      <linearGradient id="dish" x1="0" y1="0" x2="1" y2="1">
        <stop offset="0" stop-color="#c9432a"/>
        <stop offset="0.35" stop-color="#e7e0cf"/>
        <stop offset="0.6" stop-color="#b8352a"/>
        <stop offset="0.8" stop-color="#9bbf4a"/>
        <stop offset="1" stop-color="#a8322a"/>
      </linearGradient>
    </defs>
    <path d="M660 0 H1200 V599 H740 C700 520 690 420 700 300 C710 180 690 80 660 0 Z" fill="url(#dish)"/>
  </svg>

  <h1 class="menu-title">DESAYUNOS</h1>

  <div class="label col-head" style="left:335px; top:70px;">Pastor:</div>
  <div class="label col-head" style="left:540px; top:70px;">Arrachera:</div>

  <div class="label row-head" style="top:140px;">Chilaquiles:</div>
  <div class="label row-head" style="top:222px; line-height:1.25;">Tacos<br>dorados (3):</div>
  <div class="label row-head" style="top:359px;">Burritos:</div>

  <div class="price" style="left:324px; top:161px;">$45</div>
  <div class="price" style="left:544px; top:161px;">$50</div>
  <div class="price" style="left:324px; top:270px;">$40</div>
  <div class="price" style="left:544px; top:270px;">$45</div>
  <div class="price" style="left:324px; top:381px;">$45</div>
  <div class="price" style="left:544px; top:381px;">$45</div>

  <div class="label col-head" style="left:330px; top:450px;">Queso:</div>
  <div class="label col-head" style="left:545px; top:450px;">Huevo:</div>

  <div class="price" style="left:324px; top:540px;">$40</div>
  <div class="price" style="left:544px; top:540px;">$45</div>

  <div class="dot red"></div>
  <div class="dot yellow"></div>
  <div class="dot salmon"></div>
  <div class="dot cyan"></div>

  <div class="brand"><span class="brand-name">Sol<br>Gorditas</span></div>
</main>
</body>
</html>
```